Keelbrook Vault Holdings Needs A Website

We are looking for a website for a new company. 4 Pages

Needs to be responsive and mobile friendly for all browsers and coded for both Android & IOS. SEO is also important.

Website Brief – Keelbrook Vault Holdings
Domain: www.keelbrookvault.net
Email: info@keelbrookvault.net
Phone: to be inserted later
Address: 40837 52 Ave, Edmonton, AB T6K 3R8
Platform: WordPress (recommended for flexibility, SEO tools, and ease of editing)
Requirements:
• Responsive & mobile-friendly (Android & iOS)
• Cross-browser compatibility
• Fast page load speed
• SEO optimized for storage development, management, and investment keywords
• Easy in-house editing after launch
• Professional, modern, trust-driven design reflecting expertise, reliability, and innovation
________________________________________
Pages
1. HOME
Purpose: Quickly communicate who Keelbrook Vault Holdings is and why they’re the best choice for designing, building, leasing, and managing self storage facilities.
Content Highlights:
• Hero Section: Large, bold image of a modern self storage facility with headline:
"From Concept to Capacity – Your Self Storage Experts"
• Subheadline: “Keelbrook Vault Holdings delivers turnkey design, construction, leasing, and management services for profitable self storage operations.”
• Quick Service Icons:
o Facility Design & Development
o Construction & Build Management
o Lease-Up & Marketing
o Ongoing Facility Management
• Call to Action Button: “LEARN MORE” → links to ABOUT US page.
• Featured Project Highlights: Showcase a few completed or current projects with photos and stats.
• Contact Banner: “Ready to build your next self storage project? Let’s talk.” → CONTACT page.
2. ABOUT US
Purpose: Build credibility, showcase experience, and explain the value proposition.
Content Highlights:
• Who We Are: Overview of Keelbrook Vault Holdings’ history, mission, and team expertise.
• Our Approach: End-to-end process from site selection to occupancy.
• Why Choose Us:
o Industry expertise in self storage
o Proven track record in lease-up success
o Strong vendor and contractor network
3. SERVICES
Purpose: Detail all service offerings with clarity and authority.
Sections:
• Design & Development: Market analysis, site planning, and architectural design.
• Construction Management: Overseeing timelines, budgets, and quality control.
• Lease-Up Strategy: Marketing, promotions, and occupancy acceleration.
• Ongoing Facility Management: Staffing, maintenance, revenue optimization.

4. CONTACT
Purpose: Provide simple, direct ways to connect.
Content Highlights:
• Contact Form (Name, Email, Phone, Message)
• Direct Email: info@keelbrookvault.net
• Phone (if applicable)
• Google Map embed (if there’s a head office location)
• CTA: “Let’s Build Your Storage Success Story.”
Design & Technical Notes
• Visual Style: Clean, modern, bold typography, professional color palette (to be based on branding), strong imagery of self storage facilities.
• Performance: Image compression, caching, responsive scaling.
• SEO Targets: “Self storage facility developer,” “self storage construction,” “self storage management company,” “lease-up services for self storage.”

WordPress or Joomla – must be desktop and mobile friendly with fast page load speed. Need the ability to edit ourselves.

Use pantone colours - #033c5a – dark blue
#2baadf – light blue

```html
<!DOCTYPE html>
<html lang="en">
<head>
<meta charset="utf-8">
<title>About Us – Keelbrook Vault Holdings</title>
<link href="https://fonts.googleapis.com/css2?family=Montserrat:wght@600;700;800&family=Poppins:wght@400;500;600&display=swap" rel="stylesheet">
<style>
:root{
  --navy:#033c5a;
  --sky:#2baadf;
  --ink:#0a2a44;
  --text:#5b6670;
  --white:#ffffff;
  --line:#e3e7eb;
}
*{margin:0;padding:0;box-sizing:border-box}
html,body{width:1200px;height:2518px;overflow:hidden;background:var(--white)}
body{position:relative;font-family:'Poppins',sans-serif;color:var(--text)}
.abs{position:absolute}

/* header */
.site-header{left:0;top:0;width:1200px;height:90px;background:var(--white)}
.brand{left:85px;top:27px;display:flex;align-items:center;gap:10px}
.brand-square{width:30px;height:30px;background:var(--navy)}
.brand-name{font-family:'Montserrat',sans-serif;font-weight:700;font-size:20px;color:var(--navy)}
.main-nav{top:37px;left:670px;display:flex;gap:27px;font-size:13px;color:var(--ink)}
.main-nav .active{color:var(--sky);font-weight:500;padding:0 4px 6px;border-bottom:2px solid var(--sky)}
.btn-header{left:981px;top:26px;width:130px;height:38px;background:var(--sky);color:var(--white);font-family:'Montserrat',sans-serif;font-weight:700;font-size:12px;display:flex;align-items:center;justify-content:center}

/* hero */
.hero{left:0;top:91px;width:1200px;height:436px;background:linear-gradient(180deg,#b9cbdb 0%,#8e9aa6 45%,#5d6873 80%,#6f8a4f 94%,#8d8f8c 100%)}
.hero-title{left:0;top:258px;width:1200px;text-align:center;font-family:'Montserrat',sans-serif;font-weight:700;font-size:58px;color:var(--white)}

/* who we are */
.who-photo{left:165px;top:644px;width:388px;height:397px;background:linear-gradient(160deg,#6c7680,#4a535c 55%,#8ea0a8);box-shadow:0 20px 60px rgba(3,60,90,.12)}
.who-copy{left:604px;top:676px;width:405px}
.section-title{font-family:'Montserrat',sans-serif;font-weight:700;font-size:36px;color:var(--ink)}
.who-copy p{font-size:13.6px;line-height:21.5px;margin-top:10px}
.who-copy .section-title{margin-bottom:22px}
.who-copy strong{font-weight:600;color:#2f3a44}
.centered{left:0;width:1200px;text-align:center}

/* approach */
.approach-divider{left:343px;top:1233px;width:1px;height:269px;background:var(--line)}
.approach-focus{left:607px;top:1215px;width:258px;height:268px;background:var(--white);border-bottom:2px solid var(--sky);box-shadow:0 10px 40px rgba(3,60,90,.10)}
.step{top:1255px;width:240px;text-align:center}
.step svg{display:block;margin:0 auto 14px}
.step h3{font-family:'Montserrat',sans-serif;font-weight:600;font-size:17.5px;line-height:22px;color:var(--ink)}
.step p{margin:14px auto 0;font-size:13px;line-height:19.5px}
.step-wide p{width:228px}
.step-narrow p{width:196px}

/* why choose */
.reason{top:1652px;width:289px;height:335px;box-shadow:0 20px 50px rgba(3,60,90,.12)}
.reason-1{left:154px;background:linear-gradient(180deg,#3a5d80 0%,#28466a 50%,#153f62 100%)}
.reason-2{left:455px;background:linear-gradient(180deg,#8fa3b4 0%,#4f6981 50%,#173f62 100%)}
.reason-3{left:756px;background:linear-gradient(180deg,#2d6fae 0%,#1e5a8f 50%,#153f62 100%)}
.reason-copy{position:absolute;left:30px;top:242px;width:212px;color:var(--white)}
.reason-copy h3{font-family:'Montserrat',sans-serif;font-weight:700;font-size:18px}
.reason-copy p{margin-top:8px;font-size:13px;line-height:19.5px;opacity:.9}

/* cta + footer */
.footer-bg{left:0;top:2199px;width:1200px;height:319px;background:var(--navy)}
.cta{left:325px;top:2098px;width:875px;height:170px;background:var(--sky)}
.cta-text{position:absolute;left:68px;top:62px;font-family:'Montserrat',sans-serif;font-weight:700;font-size:28px;line-height:33px;color:var(--white)}
.cta-btn{position:absolute;left:637px;top:61px;width:157px;height:47px;background:var(--white);color:var(--navy);font-family:'Montserrat',sans-serif;font-weight:700;font-size:14px;display:flex;align-items:center;justify-content:center}
.footer-brand{left:93px;top:2335px;display:flex;align-items:center;gap:14px}
.footer-brand .brand-square{width:44px;height:44px;background:var(--white)}
.footer-brand .brand-name{font-size:31px;color:var(--white)}
.footer-nav{left:712px;top:2322px;display:flex;gap:37px;font-size:19px;color:var(--white)}
.footer-nav .active{font-weight:600}
.social{left:968px;top:2363px;display:flex;gap:7px}
.social span{width:30px;height:30px;border-radius:50%;background:rgba(255,255,255,.12)}
.footer-rule{left:76px;top:2462px;width:1050px;height:1px;background:rgba(255,255,255,.15)}
.copyright{left:0;top:2482px;width:1200px;text-align:center;font-size:15px;font-weight:500;color:var(--white)}
.to-top{left:1144px;top:2435px;width:40px;height:40px;border-radius:50%;background:var(--sky);display:flex;align-items:center;justify-content:center}
</style>
</head>
<body>

<header class="abs site-header">
  <div class="abs brand"><span class="brand-square"></span><span class="brand-name">Keelbrook Vault Holdings</span></div>
  <nav class="abs main-nav"><span class="active">HOME</span><span>About Us</span><span>Services</span><span>Contact</span></nav>
  <a class="abs btn-header">LEARN MORE</a>
</header>

<section class="abs hero" role="img" aria-label="Large modern self storage warehouse under a partly cloudy sky"></section>
<h1 class="abs hero-title">About US</h1>

<div class="abs who-photo" role="img" aria-label="Modern building with a metal mesh facade beside a bridge"></div>
<div class="abs who-copy">
  <h2 class="section-title">Who We Are</h2>
  <p>Keelbrook Vault Holdings is a full-service partner for entrepreneurs, investors, and property owners looking to enter or expand in the self storage market.</p>
  <p>With years of industry experience, our team has successfully designed, built, leased, and managed facilities across Western Canada.</p>
  <p>Our mission is simple: <strong>to deliver profitable, high-performing self storage facilities that stand out in their markets.</strong></p>
  <p>We combine in-depth market knowledge, operational expertise, and innovative design to ensure every project is built for long-term success.</p>
</div>

<h2 class="abs centered section-title" style="top:1126px">Our Approach</h2>
<div class="abs approach-divider"></div>
<div class="abs approach-focus"></div>

<div class="abs step step-wide" style="left:81px">
  <svg width="56" height="54" viewBox="0 0 56 54"><rect x="8" y="2" width="24" height="44" fill="var(--navy)"/><rect x="2" y="16" width="8" height="30" fill="var(--navy)"/><g fill="#fff"><rect x="13" y="8" width="4" height="4"/><rect x="21" y="8" width="4" height="4"/><rect x="13" y="16" width="4" height="4"/><rect x="21" y="16" width="4" height="4"/><rect x="13" y="24" width="4" height="4"/></g><circle cx="42" cy="40" r="11" fill="var(--sky)"/><circle cx="42" cy="40" r="4" fill="#fff"/></svg>
  <h3>Site Selection &amp;<br>Feasibility</h3>
  <p>We analyze market demand, competition, and zoning to identify the best location.</p>
</div>
<div class="abs step step-narrow" style="left:361px">
  <svg width="56" height="54" viewBox="0 0 56 54"><rect x="10" y="4" width="5" height="46" fill="var(--navy)"/><rect x="2" y="4" width="44" height="4" fill="var(--navy)"/><line x1="42" y1="8" x2="42" y2="20" stroke="var(--navy)" stroke-width="2"/><rect x="22" y="24" width="26" height="26" fill="var(--sky)"/><rect x="2" y="48" width="52" height="3" fill="var(--navy)"/></svg>
  <h3>Design &amp;<br>Development</h3>
  <p>We create efficient, customer-friendly layouts that maximize revenue potential.</p>
</div>
<div class="abs step step-narrow" style="left:616px">
  <svg width="56" height="54" viewBox="0 0 56 54"><path d="M4 18 L28 4 L52 18 V52 H4 Z" fill="var(--navy)"/><rect x="10" y="20" width="36" height="30" fill="var(--sky)"/><g stroke="#fff" stroke-width="2"><line x1="10" y1="28" x2="46" y2="28"/><line x1="10" y1="36" x2="46" y2="36"/><line x1="10" y1="44" x2="46" y2="44"/></g></svg>
  <h3>Construction &amp;<br>Build Management</h3>
  <p>We coordinate contractors, timelines, and budgets to keep your project on track.</p>
</div>
<div class="abs step step-wide" style="left:879px">
  <svg width="56" height="54" viewBox="0 0 56 54"><path d="M8 27 A20 20 0 0 1 44 15" fill="none" stroke="var(--sky)" stroke-width="3"/><path d="M48 27 A20 20 0 0 1 12 39" fill="none" stroke="var(--sky)" stroke-width="3"/><circle cx="28" cy="27" r="11" fill="var(--navy)"/><circle cx="28" cy="27" r="4" fill="#fff"/></svg>
  <h3>Lease-Up<br>&amp; Marketing</h3>
  <p>We implement strategic marketing campaigns to fill units quickly and reach profitability faster.</p>
</div>

<h2 class="abs centered section-title" style="top:1568px">Why Choose Us</h2>
<div class="abs reason reason-1" role="img" aria-label="Professional in a suit standing in an office">
  <div class="reason-copy"><h3>Industry Expertise</h3><p>Deep knowledge of self storage.</p></div>
</div>
<div class="abs reason reason-2" role="img" aria-label="Hand holding a phone over a laptop">
  <div class="reason-copy"><h3>Proven Track Record</h3><p>Fast lease-ups and high occupancy.</p></div>
</div>
<div class="abs reason reason-3" role="img" aria-label="Glass tower facade reflecting the sky">
  <div class="reason-copy"><h3>Strong Network</h3><p>Trusted vendors and contractors for quality delivery.</p></div>
</div>

<div class="abs footer-bg"></div>
<div class="abs cta">
  <p class="cta-text">Ready to build your next<br>self storage project? Let’s talk</p>
  <a class="cta-btn">LEARN MORE</a>
</div>

<div class="abs footer-brand"><span class="brand-square"></span><span class="brand-name">Keelbrook Vault Holdings</span></div>
<nav class="abs footer-nav"><span class="active">HOME</span><span>About Us</span><span>Services</span><span>Contact</span></nav>
<div class="abs social"><span></span><span></span><span></span><span></span></div>
<div class="abs footer-rule"></div>
<p class="abs copyright">© Copyright 2025. All Rights Reserved</p>
<a class="abs to-top"><svg width="10" height="6" viewBox="0 0 10 6"><path d="M1 5 L5 1 L9 5" fill="none" stroke="#fff" stroke-width="1.5"/></svg></a>

</body>
</html>
```